Corvimo Business Card

Corvimo is a young and energetic software development consultancy. We spend our time on the road working with clients on their sites an meeting new potential customers and employees!

We need a sharp, vibrant and memorable business card that will inspires those that receive it to look after it as it oozes quality and is a nice thing in its own right.

We like bold colours and distinctive design. So show us what you can do.

In terms of information on the card, it would be good to see:

* Our logo (Obviously :) )
* Employee name
* Email
* Website address
* Mobile number
* Full company name (Corvimo ltd)
* Registered company number
* Registered company address

Industry/Entity Type

Software

Requirements
Nice to have
• We are thinking that having a QR Code on the business card could be a good way of adding active marketing. It would be good to see if you are able to merge the kind of element in to your designs!

Maybe something special could be achieved using a visual QR Code like those produced at http://www.pixoranta.example/ ? You have our media so feel free to have a play.

```html
<!DOCTYPE html>
<html lang="en">
<head>
<meta charset="utf-8">
<title>Corvimo Business Card</title>
<link href="https://fonts.googleapis.com/css2?family=Open+Sans:wght@400;600;700&display=swap" rel="stylesheet">
<style>
  :root {
    --brand-red: #c0202f;
    --paper: #ffffff;
    --ink: #3a3a3a;
    --rule-grey: #b9b9b9;
    --backdrop: #e6e7ec;
  }
  * { box-sizing: border-box; margin: 0; padding: 0; }
  html, body { width: 1200px; height: 987px; overflow: hidden; }
  body {
    background: var(--backdrop);
    font-family: "Open Sans", Arial, sans-serif;
    position: relative;
  }
  .card {
    position: absolute;
    left: 220px;
    width: 760px;
    height: 434px;
    border-radius: 34px;
    overflow: hidden;
    box-shadow: 0 6px 18px rgba(0,0,0,0.12);
  }
  .card-front { top: 40px; background: var(--paper); }
  .card-back { top: 513px; background: var(--brand-red); }

  .front-swoosh { position: absolute; inset: 0; width: 100%; height: 100%; }

  .wordmark {
    position: absolute;
    font-weight: 600;
    letter-spacing: 2px;
    line-height: 1;
    text-transform: uppercase;
  }
  .card-front .wordmark {
    left: 52px; top: 78px;
    font-size: 58px;
    color: var(--brand-red);
  }
  .divider {
    position: absolute;
    left: 392px; top: 50px;
    width: 2px; height: 210px;
    background: linear-gradient(to bottom, rgba(185,185,185,0), var(--rule-grey) 30%, var(--rule-grey) 70%, rgba(185,185,185,0));
  }
  .contact-block { position: absolute; left: 428px; top: 52px; color: var(--ink); }
  .person-name { font-size: 27px; font-weight: 700; color: var(--brand-red); line-height: 1.1; }
  .person-title { font-size: 21px; line-height: 1.2; margin-bottom: 14px; }
  .contact-list { list-style: none; }
  .contact-list li { display: flex; align-items: center; gap: 8px; font-size: 20px; line-height: 1.3; }
  .contact-list svg { width: 16px; height: 16px; flex: none; }
  .office-address {
    position: absolute; left: 40px; top: 282px;
    color: var(--paper); font-size: 16px; line-height: 1.35;
  }

  .card-back .wordmark {
    left: 0; right: 0; top: 150px;
    text-align: center;
    font-size: 92px;
    color: var(--paper);
  }
  .back-url {
    position: absolute; left: 0; right: 0; top: 300px;
    text-align: center;
    color: var(--paper);
    font-size: 20px; font-weight: 600; letter-spacing: 2px;
  }
</style>
</head>
<body>

<section class="card card-front">
  <svg class="front-swoosh" viewBox="0 0 760 434" preserveAspectRatio="none" aria-hidden="true">
    <path d="M0 238 C150 240 260 300 390 372 C520 440 640 432 760 420 L760 434 L0 434 Z" fill="var(--brand-red)"/>
    <path d="M0 226 C150 228 265 288 395 360 C525 428 640 418 760 406" fill="none" stroke="var(--brand-red)" stroke-width="5"/>
    <path d="M0 250 C150 252 258 312 386 384 C520 452 640 444 760 432" fill="none" stroke="var(--paper)" stroke-width="6"/>
    <path d="M130 246 C220 262 300 318 400 372 C520 434 650 424 760 414" fill="none" stroke="#8d8d8d" stroke-width="1.5"/>
  </svg>

  <div class="wordmark">Corvimo</div>
  <div class="divider"></div>

  <div class="contact-block">
    <p class="person-name">Your Name</p>
    <p class="person-title">Title</p>
    <ul class="contact-list">
      <li>
        <svg viewBox="0 0 16 16"><circle cx="8" cy="8" r="8" fill="var(--brand-red)"/><path d="M5 4.5c0 4 2.5 7 6.5 7l.5-1.6-2-1-1 .8c-1-.5-1.7-1.2-2.2-2.2l.8-1-1-2z" fill="#fff"/></svg>
        123-456-7890
      </li>
      <li>
        <svg viewBox="0 0 16 16"><rect x="4" y="1" width="8" height="14" rx="1.5" fill="var(--brand-red)"/><rect x="5.5" y="3" width="5" height="6" fill="#fff"/></svg>
        123-456-7890
      </li>
      <li>
        <svg viewBox="0 0 16 16"><rect x="1" y="3" width="14" height="10" rx="1" fill="var(--brand-red)"/><path d="M1.5 3.5 8 9l6.5-5.5" fill="none" stroke="#fff" stroke-width="1.3"/></svg>
        info@corvimo.example
      </li>
      <li>
        <svg viewBox="0 0 16 16"><circle cx="8" cy="8" r="7.5" fill="var(--brand-red)"/><g fill="none" stroke="#fff" stroke-width="1"><ellipse cx="8" cy="8" rx="3" ry="6.5"/><path d="M1.5 8h13M2.5 5h11M2.5 11h11"/></g></svg>
        www.corvimo.example
      </li>
    </ul>
  </div>

  <address class="office-address" style="font-style:normal">
    00, Complex Name<br>City, State 0004
  </address>
</section>

<section class="card card-back">
  <div class="wordmark">Corvimo</div>
  <p class="back-url">www.corvimo.example</p>
</section>

</body>
</html>
```